8-page Visitor's Guide for Private Wildlife Ranch

We need a Visitor's Guide for Private Wildlife Ranch, where we can include important information for the clients during their stay as well as the many activities we and surrounding businesses have to offer... we are looking to keep it in line with our current web look and feel, as well as some of the included supporting documents, our rack card and our current tribe-fold brochure... I will be looking to update these as well in the near future with a supporting design... just looking for something a little more eye catching and up to date!

http:// qmrb.examplestate.test/leaflets/qmrbdocs/files/qm_lf_z7000_1111bb.

the pdf above is something we really like!!!!

Im sure you are going to need more photos, but I was limited to what I could upload!

www. kbranchhomestead. test is our website

Info about us: Are you looking for a truly unique Texas experience? K.B. Ranch Homestead is THE place! Whether you are looking for a day trip, a weekend adventure, or a place to host your next event or corporate retreat, join us at K.B. Ranch Homestead.

No matter what your needs and interests are, we offer a wide variety of activities to suit any group. K.B. Ranch Homestead has been the chosen destination for many weddings, events, and corporate retreats.

Target Market(s)

Tourism/Travel

Industry/Entity Type

Tourism

Font styles to use
Other font styles liked:
• Plantagenet Cherokee

Colors
fff3d1
ffffff

Requirements
Must have
• I have included a pdf with a lot of the text that I want.....
• Pages to include: Cover page, Important Information, Welcome Letter/Map, What to do while here, special events at the ranch, lodging options, things you might see during your stay, and a page for ads from local businesses
• colors
• 3e2a05 dark brown
• d2c0a4 light brown
• f3f2f1 light light brown
• font:
• Plantagenet Cherokee
Nice to have
• I want it to have an easy to read, rustic ranch look like with the feel of our website, but fun and exciting to make it inviting and welcoming
Should not have
• ehh pretty open to most anything but bright colors

```html
<!DOCTYPE html>
<html lang="en">
<head>
<meta charset="utf-8">
<title>K.B. Ranch Homestead – Guest Information</title>
<link rel="stylesheet" href="https://fonts.googleapis.com/css2?family=Alegreya:wght@400;500&display=swap">
<style>
  :root {
    --brown-dark: #3b2a12;
    --stone: #d8c7aa;
    --stone-deep: #cbb894;
    --panel: #d3c1a1;
    --ink: #3e2a05;
    --white: #ffffff;
  }
  * { margin: 0; padding: 0; box-sizing: border-box; }
  html, body { width: 848px; height: 1200px; overflow: hidden; }
  body { background: var(--white); font-family: "Alegreya", Georgia, serif; }
  .page {
    position: relative;
    width: 848px;
    height: 1200px;
    overflow: hidden;
    background: radial-gradient(ellipse at 40% 35%, var(--stone) 0%, var(--stone-deep) 100%);
  }
  .band {
    position: absolute;
    left: 0;
    width: 848px;
    background: var(--brown-dark);
    color: var(--white);
  }
  .band--amenities { top: 28px; height: 260px; }
  .band--activities { top: 392px; height: 392px; }
  .band-title {
    position: absolute;
    font-weight: 500;
    line-height: 1;
  }
  .band--amenities .band-title { left: 79px; top: 26px; font-size: 31px; }
  .band--activities .band-title { left: 317px; top: 13px; font-size: 33px; }
  .bullet-list { position: absolute; list-style: none; }
  .bullet-list li { position: relative; padding-left: 16px; }
  .bullet-list li::before {
    content: "";
    position: absolute;
    left: 0;
    top: 0.6em;
    width: 7px;
    height: 7px;
    border-radius: 50%;
    background: var(--white);
  }
  .amenity-list { left: 120px; top: 68px; font-size: 20px; line-height: 29.5px; }
  .amenity-list .note { display: block; line-height: 20px; margin-top: -6px; margin-bottom: 3px; }
  .activity-list { left: 354px; top: 54px; font-size: 19.5px; line-height: 29.5px; }
  .photo {
    position: absolute;
    border: 6px solid var(--white);
  }
  .photo--room {
    left: 447px; top: 20px; width: 323px; height: 217px;
    background: linear-gradient(180deg, #8d7a62 0%, #5e4c39 45%, #2e2a33 80%, #4b3a2a 100%);
  }
  .photo--wildlife {
    left: 20px; top: 23px; width: 273px; height: 347px;
    background: linear-gradient(160deg, #a9ae8c 0%, #6d6a4e 40%, #5a3b22 70%, #4d5a35 100%);
  }
  .meal-box {
    position: absolute;
    left: 111px; top: 843px;
    width: 627px; height: 297px;
    background: var(--panel);
    border: 5px solid var(--brown-dark);
    color: var(--ink);
    text-align: center;
    padding-top: 18px;
  }
  .meal-heading { font-size: 39px; font-weight: 500; line-height: 38px; margin-bottom: 8px; }
  .meal-row { font-size: 22px; line-height: 33px; }
  .meal-time { font-size: 29px; }
</style>
</head>
<body>
  <main class="page">
    <section class="band band--amenities">
      <h2 class="band-title">Room Amenities</h2>
      <ul class="bullet-list amenity-list">
        <li>Plush Bedding</li>
        <li>Shampoo/Soap</li>
        <li>Coffee Maker</li>
        <li>In Room Wifi<span class="note">(PW - 12345678)</span></li>
        <li>Hair Dryer</li>
      </ul>
      <div class="photo photo--room" role="img" aria-label="Guest room with a king bed, patterned quilt, lamps and wooden dresser"></div>
    </section>

    <section class="band band--activities">
      <div class="photo photo--wildlife" role="img" aria-label="Spotted axis deer standing behind a tree trunk"></div>
      <h2 class="band-title">Things to do in the Hill Country</h2>
      <ul class="bullet-list activity-list">
        <li>The Gallery of Frontier Arts</li>
        <li>The Hilltop Sculpture Prayer Garden</li>
        <li>Marla Keene Park</li>
        <li>Hill Country Museum/Tolliver Mansion</li>
        <li>Pecan Creek Trade Days</li>
        <li>Dance the night away at Dovewell</li>
        <li>Visit Wineries in Pecan Creek</li>
        <li>Dig for Topaz at Harlow Ranch</li>
        <li>Hike Granite Dome</li>
        <li>Heritage Museum of the Pacific Front</li>
        <li>Walter B. Hensley State Park</li>
      </ul>
    </section>

    <section class="meal-box">
      <h2 class="meal-heading">Meals are typically served<br>buffet style in our chuckwagon.</h2>
      <p class="meal-row">Breakfast is served at <span class="meal-time">8:00 AM</span></p>
      <p class="meal-row">Lunch is served at <span class="meal-time">Noon</span></p>
      <p class="meal-row">Dinner is served at <span class="meal-time">7:00 PM</span></p>
      <p class="meal-row">Open Bar from <span class="meal-time">6:00 p.m. - Midnight</span></p>
      <p class="meal-row">Snacks available for purchase in front office.</p>
    </section>
  </main>
</body>
</html>
```